Sales Flyer offering home being built and items included as well as options

We are custom home builders and we need a flyer to place in literature boxes on lots where we are building a house. Most times it's a lot and home package. But sometimes it's just a home to be built on someone lot they already own. We'd like it to list items that are included and the options being offered. It will have to have our business contact info., website info, etc.
We'd like it to have colors to go with our website and logo.
www.fendrickandloame.com. You may use some of the wording from our website if needed. We want a place to upload the house that we intend to build, which will change, (not all projects are the same house) plus maybe side stock pictures of our homes or things inside the home we have built.
This file would have to be so that it will allow us to change the sales price, items included and options from time to time and anything else that needs to changed, depending upon where we are building. I will upload an example of one we have used in the past that I did myself. But I know it can be done better

Target Market(s)

People looking for new custom home to be constructed. Usually people driving by.

Industry/Entity Type

Building

Colors

Designer to choose colors to be used in the design.

Requirements
Must have
• This is a sales flyer. Need to be professional and eye catchy, but yet elegant, pleasing to the eye.
• Our company information (see website) or current flyer uploaded.
• Website info.
• Logo (see website)
• Facebook info
• Need to be able to make changes to flyer. Can not be in just PDF
• Need to be able to print in our office, since each project changes.
• Picture of house being built, picture on flyer uploaded is the current home being offered. Must have items included and options being offered
Nice to have
• Stock pictures. Colors to go with website and logo.

```html
<!DOCTYPE html>
<html lang="en">
<head>
<meta charset="utf-8">
<title>Fendrick and Loame Custom Homes – Sales Flyer</title>
<link href="https://fonts.googleapis.com/css2?family=Anton&family=Oswald:wght@500;600&family=Open+Sans:wght@400;600&family=Cinzel:wght@500&display=swap" rel="stylesheet">
<style>
  :root{
    --page:#e9e6e1;
    --black:#0b0b0b;
    --gold-1:#f6d9a0;
    --gold-2:#c98a3c;
    --gold-3:#8a531c;
    --brown:#6e3a1a;
    --brown-text:#7a3b16;
    --tan:#e8c98e;
    --ink:#2a2320;
    --white:#ffffff;
    --band:#3a3a3a;
  }
  *{box-sizing:border-box;margin:0;padding:0}
  html,body{width:1200px;height:800px;overflow:hidden;background:var(--page)}
  body{display:flex;align-items:center;justify-content:center;font-family:"Open Sans",sans-serif}
  .flyer{position:relative;width:600px;height:776px;background:var(--white);overflow:hidden;box-shadow:0 6px 24px rgba(0,0,0,.25)}

  .masthead{position:absolute;left:0;top:0;width:600px;height:122px;background:var(--black);display:flex;align-items:center;justify-content:space-between;padding:0 22px 0 20px}
  .brand{display:flex;flex-direction:column;align-items:center;gap:6px;width:130px}
  .brand-mark{width:20px;height:20px;background:var(--gold-2)}
  .brand-name{font-family:"Cinzel",serif;font-size:11px;color:var(--gold-2);text-align:center;line-height:1.25;letter-spacing:.5px}
  .headline{font-family:"Anton",sans-serif;font-size:78px;letter-spacing:3px;line-height:1;
    background:linear-gradient(180deg,var(--gold-1) 0%,var(--gold-2) 55%,var(--gold-3) 100%);
    -webkit-background-clip:text;background-clip:text;color:transparent}

  .house-photo{position:absolute;left:0;top:122px;width:600px;height:200px;
    background:linear-gradient(180deg,#b8c0c8 0%,#9aa3ab 40%,#8a4a30 62%,#5f8a3a 80%,#4f7a30 100%)}

  .package{position:absolute;left:0;top:300px;width:600px;height:282px;background:var(--tan)}
  .price{position:absolute;left:0;top:318px;width:390px;text-align:center;font-family:"Oswald",sans-serif;font-weight:500;font-size:17px;color:var(--white);letter-spacing:.5px}
  .package-title{position:absolute;left:0;top:342px;width:390px;text-align:center;font-family:"Oswald",sans-serif;font-weight:600;font-size:21px;color:var(--brown-text)}
  .features{position:absolute;top:384px;list-style:disc;font-size:9.5px;color:var(--ink);line-height:16px;padding-left:14px}
  .features.col-a{left:26px}
  .features.col-b{left:210px;top:380px}
  .features li::marker{color:var(--brown-text)}
  .hoa-note{position:absolute;left:30px;top:566px;font-size:6px;color:var(--ink)}

  .pitch{position:absolute;left:392px;top:270px;width:208px;height:206px;background:var(--brown);color:var(--white);text-align:center;padding:24px 12px 0}
  .pitch-lines{font-family:"Open Sans",sans-serif;font-weight:600;font-size:10px;line-height:15px;text-transform:uppercase}
  .pitch-note{font-size:8px;line-height:11px;margin-top:10px}

  .company{position:absolute;left:0;top:582px;width:600px;height:140px;background:var(--white);padding:10px 24px 0}
  .company-name{font-family:"Oswald",sans-serif;font-weight:600;font-size:28px;color:var(--brown-text);letter-spacing:.3px;line-height:1.1}
  .company-details{display:flex;gap:10px;font-size:10px;color:var(--ink);margin-top:2px}
  .company-details span + span{border-left:1px solid #999;padding-left:10px}
  .tagline{font-family:"Oswald",sans-serif;font-weight:500;font-size:17px;color:var(--brown-text);margin-top:4px;letter-spacing:.5px}
  .hours{position:absolute;left:24px;top:96px;font-size:7.5px;line-height:10px;color:var(--ink)}
  .hours strong{font-size:9px;font-weight:600;display:block}
  .contacts{position:absolute;right:24px;top:78px;list-style:none;font-size:8px;line-height:13px;color:var(--ink)}
  .contacts li{display:flex;align-items:center;gap:5px}
  .contacts svg{width:9px;height:9px}

  .call-band{position:absolute;left:0;bottom:0;width:600px;height:54px;background:var(--band);display:flex;align-items:center;justify-content:center;font-family:"Anton",sans-serif;font-size:30px;color:var(--white);letter-spacing:1px}
</style>
</head>
<body>
<main class="flyer">
  <header class="masthead">
    <div class="brand">
      <span class="brand-mark"></span>
      <span class="brand-name">FENDRICK AND LOAME<br>CUSTOM HOMES</span>
    </div>
    <h1 class="headline">INCLUDED</h1>
  </header>

  <div class="house-photo" role="img" aria-label="Photo of the featured home: single-story house with tan and red siding, two-car garage, paved driveway and lawn"></div>

  <section class="package">
  </section>
  <p class="price">SALE PRICE $ 289,900</p>
  <h2 class="package-title">IN THIS LOT AND HOME PACKAGE</h2>
  <ul class="features col-a">
    <li>3 Bedroom &amp; 2 Full Baths</li>
    <li>Custom Tile Shower</li>
    <li>w/glass enclosure</li>
    <li>Gourmet Kitchen</li>
    <li>Granite Counter Top</li>
    <li>Stainless Steel Appliances</li>
    <li>Hardwood and tile floors</li>
    <li>Carpet in Bedrooms</li>
  </ul>
  <ul class="features col-b">
    <li>9' Ceilings</li>
    <li>36" Propane Fireplace</li>
    <li>Custom Trim Pkg.</li>
    <li>Crown molding included</li>
    <li>Custom Painting</li>
    <li>Septic &amp; Well</li>
    <li>Asphalt driveway</li>
    <li>Rennick Tankless Water Heater</li>
  </ul>
  <p class="hoa-note">*HOA ONLY $285 PER YEAR</p>

  <aside class="pitch">
    <p class="pitch-lines">Your design or ours!<br>We will design and build your<br>dream home!<br>Bring your design we<br>will build it<br>Building homes<br>Building relationships</p>
    <p class="pitch-note">Ours teams knows that true success<br>is grounded in the relationships you<br>create.</p>
  </aside>

  <section class="company">
    <h2 class="company-name">FENDRICK AND LOAME CUSTOM HOMES</h2>
    <p class="company-details"><span>1187 MARROW LN</span><span>HARLOW CREEK, DE 19960</span><span>302-555-0148</span></p>
    <p class="tagline">BUILDING HOMES * BUILDING RELATIONSHIPS</p>
    <div class="hours">
      <strong>OFFICE HOURS</strong>
      9A.M. - 4 P.M. Monday - Friday<br>
      BY APPOINTMENT (Sat. &amp; Sun.)<br>
      Check out our video - www.fendrickandloame.com
    </div>
    <ul class="contacts">
      <li><svg viewBox="0 0 10 10"><circle cx="5" cy="5" r="4" fill="none" stroke="#2a2320" stroke-width="1"/><line x1="1" y1="5" x2="9" y2="5" stroke="#2a2320" stroke-width=".8"/><ellipse cx="5" cy="5" rx="2" ry="4" fill="none" stroke="#2a2320" stroke-width=".8"/></svg>www.fendrickandloame.com</li>
      <li><svg viewBox="0 0 10 10"><rect x="1" y="2" width="8" height="6" fill="none" stroke="#2a2320" stroke-width="1"/><polyline points="1,2 5,6 9,2" fill="none" stroke="#2a2320" stroke-width="1"/></svg>fendrickloame@mail.com</li>
      <li><svg viewBox="0 0 10 10"><rect x="1" y="1" width="8" height="8" fill="#2a2320"/></svg>/FendrickLoameCustomHomes</li>
    </ul>
  </section>

  <footer class="call-band">CALL US ANYTIME: 302-555-0148</footer>
</main>
</body>
</html>
```